Patient Recruitment Presentation for a Clinical Trial

We need a powerpoint designed to recruit patients for a clinical trial. We need 4 slides designed: an opening slide, two body slides, and an end slide. The opening slide should include the question, "Do you suffer from Depression?" in the middle of the screen, but other than that just include the design, graphic, or texture that you develop. The 2 body slides should allow for the title of study (please use “Depression Research Study”) to be across the top and contact information (phone number, URL) to be on the bottom of the slide, either centered or left or right justified. Whether this text (study title and contact information) is set off by a banner or shape that stretches across the entire slide or just provides a background to that text is up to you. One of the two body slides should include the attached horizontal stock image with a clear section to insert text either beside or over the top of the negative space of the image. This image should be stretch to the full width of the screen. The second body slide should include the attached vertical stock image, with a clear section to insert text beside the picture. (You can crop vertical portions of the images if needed.)

The end slide should resemble the opening slide in terms of design, yet this time includes the study title and contact information prominently displayed.

In terms of design, we’re looking for something clean and trustworthy, and even though this is medical, we don’t want any pills, test tubes, or heart rate lines. We’re trying to give people hope, so we want to earn their trust by communicating quality and excellence.

Please see the attached examples of the types of designs and layouts we like, how the images need to be treated, and places for text need to be designed.

We need the design to be 1920x1080 pixels, and we need the slides delivered as layered PSD files so we can manipulate as needed.

Thanks!

Target Market(s)

Adults in the US that are not working full time and able to participate in a research study.

Industry/Entity Type

Medical

Font styles to use
Serif
Sans Serif

Requirements
Must have
• The design must use the two images attached as specified in the brief. Other than that, I'm open to your creative interpretation.
Nice to have
• Nice clean design, clean fonts, nice color palette.
Should not have
• Images or designs relating to the medical world, no test tubes, heart rate lines, images of doctors or pills, etc.

```html
<!DOCTYPE html>
<html lang="en">
<head>
<meta charset="UTF-8">
<title>Depression Research Study – Opening Slide</title>
<link rel="stylesheet" href="https://fonts.googleapis.com/css2?family=Bebas+Neue&family=Open+Sans:wght@700&family=PT+Sans:ital@1&display=swap">
<style>
  :root {
    --board-bg: #212121;
    --slide-cream: #f8f6f0;
    --slide-warm: #f6e6dc;
    --slide-mint: #dcecea;
    --slide-teal: #a9d3d3;
    --band-indigo: #3c4185;
    --headline-grey: #5b5b5b;
    --frame-grey: #555555;
    --body-grey: #5f5f5f;
    --label-white: #ffffff;
  }
  * { margin: 0; padding: 0; box-sizing: border-box; }
  html, body {
    width: 1200px;
    height: 839px;
    overflow: hidden;
    background: var(--board-bg);
  }
  .board {
    position: relative;
    width: 1200px;
    height: 839px;
  }
  .slide {
    position: absolute;
    left: 26px;
    top: 57px;
    width: 1140px;
    height: 641px;
    overflow: hidden;
    box-shadow: 0 18px 30px rgba(0, 0, 0, 0.55);
    background:
      radial-gradient(ellipse 380px 320px at 150px 170px, rgba(246, 220, 205, 0.75), transparent 70%),
      radial-gradient(ellipse 520px 300px at 560px 90px, rgba(255, 255, 252, 0.95), transparent 75%),
      linear-gradient(100deg, var(--slide-cream) 0%, #eef0ea 40%, var(--slide-mint) 65%, var(--slide-teal) 100%);
  }
  .slide__texture {
    position: absolute;
    inset: 0;
    background:
      linear-gradient(180deg, transparent 55%, rgba(170, 205, 200, 0.35) 100%);
  }
  .title-frame {
    position: absolute;
    left: 358px;
    top: 229px;
    width: 475px;
    height: 128px;
    border: 1px solid var(--frame-grey);
    text-align: center;
    color: var(--headline-grey);
    font-family: "Bebas Neue", "Oswald", sans-serif;
  }
  .title-frame__main {
    display: block;
    margin-top: 14px;
    font-size: 62px;
    line-height: 56px;
    letter-spacing: -0.5px;
  }
  .title-frame__sub {
    display: block;
    margin-top: 4px;
    font-size: 29px;
    line-height: 30px;
    letter-spacing: 4px;
  }
  .title-shadow {
    position: absolute;
    left: 368px;
    top: 374px;
    width: 455px;
    height: 22px;
    border-radius: 50%;
    background: radial-gradient(ellipse at center, rgba(120, 120, 120, 0.45) 0%, rgba(120, 120, 120, 0.15) 50%, transparent 72%);
  }
  .intro-text {
    position: absolute;
    left: 340px;
    top: 410px;
    width: 530px;
    text-align: center;
    font-family: "PT Sans", "Open Sans", sans-serif;
    font-style: italic;
    font-size: 14.5px;
    line-height: 19px;
    color: var(--body-grey);
  }
  .footer-band {
    position: absolute;
    left: 0;
    bottom: 0;
    width: 100%;
    height: 28px;
    background: var(--band-indigo);
  }
  .slide-label {
    position: absolute;
    left: 0;
    top: 734px;
    width: 1282px;
    text-align: center;
    font-family: "Open Sans", sans-serif;
    font-weight: 700;
    font-size: 40px;
    line-height: 52px;
    letter-spacing: 0.5px;
    color: var(--label-white);
  }
</style>
</head>
<body>
  <main class="board">
    <section class="slide">
      <div class="slide__texture" role="img" aria-label="Soft faceted low-poly texture in cream and mint tones"></div>
      <h1 class="title-frame">
        <span class="title-frame__main">Do you suffer</span>
        <span class="title-frame__sub">from depression?</span>
      </h1>
      <div class="title-shadow"></div>
      <p class="intro-text">Lorem ipsum dolor sit amet, consectetur adipiscing elit, sed do eiusmod<br>tempor incididunt ut labore et</p>
      <div class="footer-band"></div>
    </section>
    <p class="slide-label">OPENING</p>
  </main>
</body>
</html>
```